Label Design for Sunny Harbor - A new Fishfood label

Our company is starting with a new line of Fishfood. Till now we have a Rodentfood label, in the near future (weeks) we also will be requiring labels for dog, cat and birdfood. We like to have a long term collaboration with the designer that wins this com

```html
<!DOCTYPE html>
<html lang="en">
<head>
<meta charset="utf-8">
<title>Sunny Harbor Fish Food Label</title>
<link rel="stylesheet" href="https://fonts.googleapis.com/css2?family=Baloo+2:wght@800&family=Bree+Serif&family=Lora:ital,wght@1,500&family=Oswald:wght@600&family=Libre+Franklin:wght@400;700;900&display=swap">
<style>
  :root {
    --deep: #031634;
    --ocean: #0a3a86;
    --ocean-light: #1f73c9;
    --gravel: #1b3fd0;
    --gravel-bright: #2447e6;
    --band-red: #e8321a;
    --band-orange: #f5801f;
    --band-yellow: #ffb53a;
    --logo-blue: #0f4f9c;
    --pink: #e2307c;
    --green: #1b8a2b;
    --gold: #f7a21c;
    --koi-red: #d8381f;
    --rock: #2d4a63;
    --white: #ffffff;
    --ink: #111111;
    --badge-red: #d5161e;
    --badge-blue: #1560b8;
    --badge-orange: #ef8a1c;
  }
  * { margin: 0; padding: 0; box-sizing: border-box; }
  html, body { width: 1200px; height: 686px; overflow: hidden; background: var(--deep); }
  .label { position: relative; width: 1200px; height: 686px; overflow: hidden; }

  .aquarium-scene {
    position: absolute; inset: 0;
    background:
      radial-gradient(ellipse 420px 380px at 560px 330px, rgba(80,170,255,.55), transparent 70%),
      linear-gradient(180deg, var(--deep) 0%, var(--ocean) 45%, #0b2e74 72%, var(--gravel) 88%, #0f2ca8 100%);
  }
  .gravel-bed {
    position: absolute; left: 0; right: 0; top: 600px; bottom: 0;
    background: linear-gradient(180deg, rgba(36,71,230,0) 0%, var(--gravel-bright) 35%, var(--gravel) 100%);
  }
  .fish-and-rocks {
    position: absolute; inset: 0;
    background:
      radial-gradient(ellipse 110px 52px at 440px 488px, rgba(247,162,28,.95), rgba(247,162,28,0) 75%),
      radial-gradient(ellipse 88px 58px at 712px 388px, rgba(247,162,28,.95), rgba(247,162,28,0) 75%),
      radial-gradient(ellipse 22px 30px at 580px 275px, rgba(247,162,28,.9), rgba(247,162,28,0) 75%),
      radial-gradient(ellipse 30px 20px at 1016px 272px, rgba(247,162,28,.9), rgba(247,162,28,0) 75%),
      radial-gradient(ellipse 26px 24px at 140px 392px, rgba(247,162,28,.9), rgba(247,162,28,0) 75%),
      radial-gradient(ellipse 40px 24px at 58px 432px, rgba(216,56,31,.85), rgba(216,56,31,0) 75%),
      radial-gradient(ellipse 46px 16px at 178px 452px, rgba(230,230,230,.8), rgba(230,230,230,0) 75%),
      radial-gradient(ellipse 40px 20px at 524px 458px, rgba(216,56,31,.85), rgba(216,56,31,0) 75%),
      radial-gradient(ellipse 46px 16px at 622px 550px, rgba(216,56,31,.8), rgba(216,56,31,0) 75%),
      radial-gradient(ellipse 56px 14px at 790px 470px, rgba(120,120,110,.8), rgba(120,120,110,0) 75%),
      radial-gradient(ellipse 32px 18px at 924px 503px, rgba(216,56,31,.8), rgba(216,56,31,0) 75%),
      radial-gradient(ellipse 105px 34px at 510px 610px, rgba(235,228,210,.9), rgba(235,228,210,0) 75%),
      radial-gradient(ellipse 46px 120px at 690px 540px, rgba(45,74,99,.95), rgba(45,74,99,0) 80%),
      radial-gradient(ellipse 40px 50px at 410px 600px, rgba(45,74,99,.9), rgba(45,74,99,0) 80%);
  }
  .swoosh { position: absolute; inset: 0; }

  .brand { position: absolute; font-family: "Baloo 2", sans-serif; font-weight: 800; color: var(--logo-blue); line-height: .82; text-align: center; }
  .brand--main { left: 400px; top: 40px; width: 380px; font-size: 96px; }
  .brand--corner { left: 980px; top: 30px; width: 170px; font-size: 40px; }
  .brand--side { left: 12px; top: 184px; width: 232px; font-size: 54px; }

  .barcode-caption { position: absolute; left: 966px; top: 206px; width: 214px; font-family: "Libre Franklin", sans-serif; font-size: 15px; letter-spacing: 4px; color: var(--ink); text-align: center; }

  .product-line { position: absolute; top: 270px; font-family: "Bree Serif", serif; font-size: 50px; letter-spacing: 1px; -webkit-text-stroke: 2px var(--white); paint-order: stroke fill; }
  .product-line--soft { left: 284px; color: var(--pink); }
  .product-line--variety { left: 612px; color: var(--green); }

  .tagline { position: absolute; left: 296px; top: 336px; width: 300px; font-family: "Lora", serif; font-style: italic; font-size: 25px; line-height: 36px; color: var(--white); text-align: center; }

  .badge { position: absolute; border-radius: 50%; border: 3px solid var(--white); display: flex; align-items: center; justify-content: center; text-align: center; font-family: "Oswald", sans-serif; color: var(--white); line-height: 1.05; box-shadow: 0 2px 6px rgba(0,0,0,.45); }
  .badge--sizes { left: 781px; top: 490px; width: 78px; height: 78px; background: var(--badge-red); font-size: 13px; }
  .badge--vitamin { left: 752px; top: 562px; width: 76px; height: 76px; background: var(--badge-blue); font-size: 12px; }
  .badge--easy { left: 834px; top: 560px; width: 76px; height: 76px; background: var(--badge-orange); font-size: 12px; }

  .nutrition-panel { position: absolute; left: 954px; top: 308px; width: 234px; height: 364px; background: var(--white); border: 2px solid var(--ink); padding: 3px 5px; font-family: "Libre Franklin", sans-serif; color: var(--ink); font-size: 11px; overflow: hidden; }
  .nutrition-panel h2 { font-weight: 900; font-size: 28px; line-height: 28px; letter-spacing: -.5px; }
  .nutrition-panel .serving { font-size: 11px; border-bottom: 8px solid var(--ink); padding-bottom: 2px; }
  .row { display: flex; justify-content: space-between; border-top: 1px solid var(--ink); padding: 2px 0; line-height: 12px; }
  .row--first { border-top: none; font-weight: 700; font-size: 10px; }
  .row--calories { border-bottom: 4px solid var(--ink); }
  .row--indent { padding-left: 12px; }
  .row--dv { justify-content: flex-end; font-weight: 700; }
  .row--thick { border-bottom: 8px solid var(--ink); }
  .nutrition-panel b { font-weight: 700; }
  .footnote { font-size: 9px; line-height: 11px; padding-top: 3px; border-top: 1px solid var(--ink); }
  .source { margin-top: 4px; border: 1px solid var(--ink); background: #e2e2e2; text-align: center; font-weight: 700; font-size: 10px; padding: 1px 0; }

  .supplement-panel { position: absolute; left: 42px; top: 486px; width: 194px; height: 186px; background: var(--white); padding: 3px 5px; font-family: "Libre Franklin", sans-serif; color: var(--ink); font-size: 5.6px; line-height: 6.6px; overflow: hidden; }
  .supplement-panel h3 { font-size: 15px; line-height: 17px; font-weight: 700; text-align: center; }
  .supplement-panel .head { display: flex; justify-content: space-between; border-top: 1px solid var(--ink); border-bottom: 2px solid var(--ink); }
  .supplement-panel .item { display: grid; grid-template-columns: 1fr 34px 26px; border-bottom: .5px solid #777; }
  .supplement-panel .item span:not(:first-child) { text-align: right; }
  .supplement-panel .other { margin-top: 2px; border-top: 1px solid var(--ink); padding-top: 1px; }
</style>
</head>
<body>
<main class="label">
  <div class="aquarium-scene"></div>
  <div class="gravel-bed"></div>
  <div class="fish-and-rocks" role="img" aria-label="Goldfish and koi swimming around rock ornaments above blue aquarium gravel"></div>

  <svg class="swoosh" viewBox="0 0 1200 686" width="1200" height="686" aria-hidden="true">
    <defs>
      <linearGradient id="bandFill" x1="0" y1="0" x2="1" y2="0">
        <stop offset="0" stop-color="var(--band-red)"/>
        <stop offset=".45" stop-color="var(--band-orange)"/>
        <stop offset="1" stop-color="var(--band-yellow)"/>
      </linearGradient>
    </defs>
    <path d="M0 142 Q 520 20 1200 8 L1200 206 Q 520 240 0 365 Z" fill="url(#bandFill)"/>
    <path d="M0 142 Q 520 20 1200 8" fill="none" stroke="var(--white)" stroke-width="3"/>
    <path d="M0 365 Q 520 240 1200 206" fill="none" stroke="var(--white)" stroke-width="4"/>
  </svg>

  <div class="brand brand--main">Sunny<br>Harbor</div>
  <div class="brand brand--corner">Sunny<br>Harbor</div>
  <div class="brand brand--side">Sunny<br>Harbor</div>

  <div class="barcode-caption">SUNNY HARBOR</div>

  <div class="product-line product-line--soft">Soft Sticks</div>
  <div class="product-line product-line--variety">Variety Sticks</div>

  <p class="tagline">a blend of foods<br>for increased vitality</p>

  <div class="badge badge--sizes">ALL SIZES<br>OF POND<br>FISH</div>
  <div class="badge badge--vitamin">VITAMIN<br>ENRICHED</div>
  <div class="badge badge--easy">EASY TO<br>EAT AND<br>DIGEST</div>

  <section class="supplement-panel">
    <h3>Supplement Facts</h3>
    <div class="head"><span>Serving Size 10 sticks</span><span>Amount per serving</span><span>%DV</span></div>
    <div class="item"><span>Vitamin A</span><span>250IU</span><span>50%</span></div>
    <div class="item"><span>Vitamin C</span><span>8mg</span><span>125%</span></div>
    <div class="item"><span>Vitamin D3</span><span>40IU</span><span>100%</span></div>
    <div class="item"><span>Vitamin E</span><span>3IU</span><span>100%</span></div>
    <div class="item"><span>Thiamin</span><span>0.2mg</span><span>100%</span></div>
    <div class="item"><span>Riboflavin</span><span>0.2mg</span><span>100%</span></div>
    <div class="item"><span>Niacin</span><span>1.6mg</span><span>80%</span></div>
    <div class="item"><span>Vitamin B6</span><span>0.2mg</span><span>100%</span></div>
    <div class="item"><span>Folic acid</span><span>40mcg</span><span>100%</span></div>
    <div class="item"><span>Vitamin B12</span><span>0.6mcg</span><span>100%</span></div>
    <div class="item"><span>Biotin</span><span>3mcg</span><span>10%</span></div>
    <div class="item"><span>Pantothenic acid</span><span>1mg</span><span>100%</span></div>
    <div class="item"><span>Calcium</span><span>16mg</span><span>16%</span></div>
    <div class="item"><span>Iodine</span><span>15mcg</span><span>100%</span></div>
    <div class="item"><span>Zinc</span><span>1.5mg</span><span>100%</span></div>
    <div class="item"><span>Selenium</span><span>2mcg</span><span>29%</span></div>
    <div class="item"><span>Copper</span><span>0.2mg</span><span>100%</span></div>
    <div class="item"><span>Manganese</span><span>0.2mg</span><span>100%</span></div>
    <div class="item"><span>Astaxanthin</span><span>5mg</span><span>&dagger;</span></div>
    <p class="other">Other ingredients: fish meal, wheat germ, spirulina, krill meal, garlic, kelp.</p>
  </section>

  <section class="nutrition-panel">
    <h2>Nutrition Facts</h2>
    <p class="serving">Serving Size 10 sticks per 100 g fish (2 g)</p>
    <div class="row row--first"><span>Amount Per Serving</span></div>
    <div class="row row--calories"><span><b>Calories</b> 7</span><span>Calories from Fat 2</span></div>
    <div class="row row--dv"><span>% Daily Value*</span></div>
    <div class="row"><span><b>Crude Fat</b> 0.2g</span><b>17%</b></div>
    <div class="row row--indent"><span>Omega-3 Fatty Acids 0.03g</span><b>6%</b></div>
    <div class="row row--indent"><span>Trans Fat 0g</span><span></span></div>
    <div class="row"><span><b>Moisture</b> 0.2g</span><b>0%</b></div>
    <div class="row"><span><b>Phosphorus</b> 18mg</span><b>1%</b></div>
    <div class="row"><span><b>Total Carbohydrate</b> 0.6g</span><b>19%</b></div>
    <div class="row row--indent"><span>Crude Fiber 0.1g</span><b>43%</b></div>
    <div class="row row--indent"><span>Ash 0.2g</span><span></span></div>
    <div class="row row--thick"><span><b>Crude Protein</b> 0.8g</span><span></span></div>
    <div class="row"><span>Vitamin A &nbsp;&nbsp;30% &bull; Vitamin C</span><span>54%</span></div>
    <div class="row"><span>Calcium &nbsp;&nbsp;&nbsp;&nbsp;10% &bull; Iron</span><span>28%</span></div>
    <p class="footnote">*Percent Daily Values are based on the needs of adult pond fish. Feed 2&ndash;3 times daily, only what is eaten within 3 minutes.</p>
    <p class="source">&copy;www.FeedFactsHub.com</p>
  </section>
</main>
</body>
</html>
```